"Turn The Light" Dance Production Poster

This is a dance school annual theatre performance, at the Holloway Grand Theatre. The dates are from the 26th-28th July 2012, and the show is called "Turn The Light."

Although not themed around Desmond Harlow specifically, we are using a few songs hence the title.

We need an eye catching poster with out focusing too much around DH. Maybe even using his theme/image subliminally but must look professional and vivid.

We are a dance school predominantly female based with a few males - age range 2-55
Updates

Hi guys - please check brief 

We are getting to many designs based too much around Desmond Harlow

This only has to be subliminal as the show isn't about him, it's mainly a generic dance show

Please try to bare this in mind

Thanks

Target Market(s)

Parents, family, friends of the performers/general public

Industry/Entity Type

School

Requirements
Must have
• The Wendell Moss School Of Dance Present "Turn The Light"
26th-28th July 2012 at the Holloway Grand

Tickets available from the Theatre Box Office

www.wmschoolofdance-example.co.uk

Nice to have
• Subliminal Desmond Harlow feel - no pictures of him though
Should not have
• Cheap templates, poor images, flowery fonts

```html
<!DOCTYPE html>
<html lang="en">
<head>
<meta charset="utf-8">
<title>Turn The Light – The Wendell Moss School Of Dance</title>
<link rel="stylesheet" href="https://fonts.googleapis.com/css2?family=Open+Sans:ital,wght@0,400;0,600;0,700;1,400&family=Noto+Serif:wght@400&display=swap">
<style>
  :root {
    --night: #141516;
    --night-deep: #0c0d0e;
    --steel: #2a4557;
    --steel-light: #30506a;
    --band: #386a92;
    --white: #ffffff;
    --glow: #5f9fd6;
  }
  html, body {
    margin: 0;
    padding: 0;
    overflow: hidden;
    background: var(--night);
  }
  .poster {
    position: relative;
    width: 848px;
    height: 1200px;
    overflow: hidden;
    background: linear-gradient(160deg, var(--night) 0%, var(--night-deep) 100%);
    font-family: "Open Sans", Arial, sans-serif;
    color: var(--white);
  }
  .backdrop {
    position: absolute;
    inset: 0;
  }
  .dancer-art {
    position: absolute;
    left: 280px;
    top: 470px;
    width: 568px;
    height: 520px;
    background:
      radial-gradient(ellipse 90px 150px at 460px 220px, rgba(255,255,255,0.95) 0%, rgba(190,220,255,0.5) 35%, rgba(60,110,160,0) 100%),
      linear-gradient(90deg, rgba(120,170,210,0) 0%, rgba(150,195,230,0.35) 55%, rgba(120,170,210,0) 100%) 0 110px / 100% 60px no-repeat,
      radial-gradient(ellipse 200px 260px at 440px 250px, rgba(40,70,95,0.7) 0%, rgba(20,25,30,0) 100%);
  }
  .school {
    position: absolute;
    top: 42px;
    left: 0;
    width: 100%;
    margin: 0;
    text-align: center;
    font-weight: 600;
    font-size: 63px;
    line-height: 80px;
    letter-spacing: 0.5px;
    text-shadow: 0 0 8px rgba(0,0,0,0.8);
  }
  .present {
    position: absolute;
    top: 222px;
    left: 0;
    width: 100%;
    text-align: center;
    font-style: italic;
    font-size: 41px;
    padding-left: 40px;
    box-sizing: border-box;
  }
  .show-title {
    position: absolute;
    top: 300px;
    left: 0;
    width: 100%;
    margin: 0;
    text-align: center;
    padding-left: 40px;
    box-sizing: border-box;
    font-family: "Noto Serif", Georgia, serif;
    font-weight: 400;
    font-size: 88px;
    line-height: 120px;
    white-space: nowrap;
    text-shadow: 0 0 6px var(--glow), 0 0 16px var(--glow), 0 0 26px rgba(95,159,214,0.6);
  }
  .dates {
    position: absolute;
    left: 36px;
    top: 862px;
  }
  .dates-days {
    display: inline-block;
    font-weight: 700;
    font-size: 62px;
    line-height: 70px;
    border-bottom: 3px solid var(--band);
  }
  .dates-month {
    display: block;
    font-size: 62px;
    line-height: 70px;
  }
  .venue {
    position: absolute;
    left: 34px;
    top: 1012px;
    font-size: 48px;
    line-height: 60px;
  }
  .tickets-band {
    position: absolute;
    left: 20px;
    top: 1080px;
    width: 808px;
    height: 92px;
    background: var(--band);
    text-align: center;
    font-style: italic;
  }
  .tickets-note {
    display: block;
    padding-top: 10px;
    font-size: 24px;
    line-height: 32px;
  }
  .tickets-web {
    display: block;
    font-size: 30px;
    line-height: 40px;
  }
</style>
</head>
<body>
<div class="poster">
  <svg class="backdrop" width="848" height="1200" viewBox="0 0 848 1200" aria-hidden="true">
    <circle cx="-485" cy="560" r="900" fill="var(--steel)"/>
    <polygon points="0,515 848,1010 848,1200 0,1200" fill="var(--steel-light)" opacity="0.85"/>
  </svg>

  <div class="dancer-art" role="img" aria-label="Silhouette of a dancer in a hat, lit by a bright white glow with light streaks trailing to the left"></div>

  <h1 class="school">The Wendell Moss<br>School Of Dance</h1>
  <div class="present">Present</div>
  <h2 class="show-title">"Turn The Light"</h2>

  <div class="dates">
    <span class="dates-days">26th-28th</span>
    <span class="dates-month">JULY 2012</span>
  </div>
  <div class="venue">HOLLOWAY GRAND</div>

  <div class="tickets-band">
    <span class="tickets-note">Tickets available from the Theatre Box Office</span>
    <span class="tickets-web">www.wmschoolofdance-example.co.uk</span>
  </div>
</div>
</body>
</html>
```